Social Media Cover and Profile

We already have our own logo. We just need a fresh design on our social media pages. We are not happy with our current designs. We would like to incorporate our YIKE billboard and the colors are blue (#05143f) and white. You can also incorporate silver as well. We are a family law office (Divorce and Custody) We no longer want to incorporate the Spire of Dunvale photo that we are currently using. You can look at our Facebook page; The Law Office of Miles T. Hadley.

Target Market(s)

Potential Clients

Industry/Entity Type

Family Law

Logo Text

Our Logo Is The Law Office of Miles T. Hadley with the Sheild

Requirements
Must have
• Text to include:
Central Pennslyvania's Premier Family Law Firm

Ability to be resized to and used as all images in social media, including but not limited to: Youtube Channel art, Facebook Cover and Profile.
Nice to have
• Darker color but we are open to "bright" ideas.

```html
<!DOCTYPE html>
<html lang="en">
<head>
<meta charset="utf-8">
<title>Hadley Family Law – Social Cover</title>
<link href="https://fonts.googleapis.com/css2?family=Poppins:wght@400;600;700&display=swap" rel="stylesheet">
<style>
  :root {
    --navy: #05143f;
    --white: #ffffff;
    --silver-light: #e9eaed;
    --silver-mid: #d6d8dc;
    --ink: #111111;
  }
  * { margin: 0; padding: 0; box-sizing: border-box; }
  html, body { width: 1200px; height: 457px; overflow: hidden; background: var(--white); }
  .cover {
    position: relative;
    width: 1200px;
    height: 457px;
    overflow: hidden;
    background: var(--white);
    font-family: "Poppins", sans-serif;
  }
  .cover__shapes { position: absolute; inset: 0; }
  .cover__column {
    position: absolute;
    right: 8px;
    top: 0;
    width: 108px;
    height: 457px;
    background: linear-gradient(90deg, #cfd1d4 0%, #f6f6f7 35%, #e3e4e6 60%, #b9bbbf 100%);
  }
  .cover__copy {
    position: absolute;
    left: 636px;
    width: 460px;
    top: 132px;
    text-align: center;
    color: var(--ink);
  }
  .cover__kicker {
    font-weight: 400;
    font-size: 25px;
    line-height: 1.2;
    letter-spacing: 0.2px;
  }
  .cover__headline {
    margin-top: 8px;
    font-weight: 700;
    font-size: 50px;
    line-height: 1.1;
    letter-spacing: -0.3px;
  }
  .brand-name {
    margin-top: 26px;
    font-weight: 600;
    font-size: 34px;
    line-height: 1;
    color: var(--ink);
  }
  .brand-row {
    margin-top: 16px;
    display: flex;
    justify-content: center;
    align-items: center;
    gap: 14px;
  }
  .brand-row__office {
    display: flex;
    align-items: center;
    gap: 5px;
    font-weight: 600;
    font-size: 10px;
    line-height: 1.1;
    color: var(--navy);
    text-transform: uppercase;
    text-align: left;
    max-width: 130px;
  }
  .brand-row__square {
    width: 14px;
    height: 14px;
    background: var(--navy);
    flex: none;
  }
  .brand-row__web {
    font-weight: 600;
    font-size: 12px;
    color: var(--ink);
  }
</style>
</head>
<body>
  <main class="cover">
    <svg class="cover__shapes" width="1200" height="457" viewBox="0 0 1200 457" aria-hidden="true">
      <defs>
        <linearGradient id="woodTone" x1="0" y1="0" x2="1" y2="1">
          <stop offset="0" stop-color="#8a6444"/>
          <stop offset="0.5" stop-color="#a97e57"/>
          <stop offset="1" stop-color="#6b4a2f"/>
        </linearGradient>
      </defs>
      <polygon points="620,0 850,0 890,100 660,100" fill="var(--silver-light)"/>
      <polygon points="1040,457 1200,250 1200,457" fill="var(--silver-light)"/>
      <polygon points="400,0 470,0 700,457 630,457" fill="var(--silver-mid)" opacity="0.6"/>
    </svg>

    <svg class="cover__shapes" width="1200" height="457" viewBox="0 0 1200 457">
      <polygon role="img" aria-label="Photo of a judge's gavel on a wooden desk beside a leather book"
               points="0,0 415,0 645,457 0,457" fill="url(#woodTone)"/>
      <polygon points="250,0 330,0 560,457 480,457" fill="var(--white)" opacity="0.28"/>
      <polygon points="0,248 178,457 0,457" fill="var(--navy)"/>
    </svg>

    <div class="cover__column" role="img" aria-label="White classical column"></div>

    <section class="cover__copy">
      <p class="cover__kicker">Central Pennslyvania's Premier</p>
      <h1 class="cover__headline">Family Law Firm</h1>
      <p class="brand-name">YIKE</p>
      <div class="brand-row">
        <span class="brand-row__office"><span class="brand-row__square"></span>The Law Office of Miles T. Hadley</span>
        <span class="brand-row__web">HadleyDivorce.com</span>
      </div>
    </section>
  </main>
</body>
</html>
```